Vantor Roving Car Wash and Detail Services, 'needs a logo and card design'

I need a logo and Card design for a new company based in Perth Western Australia called, 'Vantor Roving Car Wash and Detail Services'. I want to offer a mobile car wash and detail service across all the Perth metropolitan areas at lower prices, and offer more reliability. I would like to see designs with colours such as red, white, and black. The final design should communicate trust reliability and confidence in the services I can provide. The card must include my first name 'Oswin' and my mobile number '0471208356' for an obligation free quote.
Updates

Target Market(s)

Aimed at anyone who owns and drives a motor vehicle.

Industry/Entity Type

It Company

Contact Information for Business Card

Business Name'Vantor Roving Car Wash and Detail Services', My first name 'Oswin', and my mobile phone '0471208356' for an obligation free quote.

Font styles to use
Serif
Decorative
Script

Colors
ffffff
000000
d3d3d3
ec1f27
7f7f7f

Requirements
Must have
• Business Name'Vantor Roving Car Wash and Detail Services', My first name 'Oswin', and my mobile phone '0471208356' for an obligation free quote.
• Logo design
Nice to have
• A slogan, such as 'I come to you, and wash your car wherever you are' to let customers know I am at their service.
• Car design 'shine and clean feeling'

```html
<!DOCTYPE html>
<html lang="en">
<head>
<meta charset="utf-8">
<title>Vantor Roving Car Wash and Detail Services – Business Card</title>
<link rel="stylesheet" href="https://fonts.googleapis.com/css2?family=Open+Sans:wght@400;600;700&display=swap">
<style>
  :root {
    --backdrop: #2f2f2f;
    --aqua: #5ccbdc;
    --aqua-deep: #4fc1d3;
    --paper: #f4f4f4;
    --paper-shade: #e6e6e6;
    --ink: #555557;
    --white: #ffffff;
  }
  * { margin: 0; padding: 0; box-sizing: border-box; }
  html, body {
    width: 1200px;
    height: 900px;
    overflow: hidden;
    background: var(--backdrop);
    font-family: "Open Sans", Arial, sans-serif;
  }
  .canvas {
    position: relative;
    width: 1200px;
    height: 900px;
  }
  .card {
    position: absolute;
    width: 560px;
    height: 320px;
    border-radius: 22px;
    box-shadow: 0 14px 30px rgba(0, 0, 0, 0.45);
  }
  .card--front {
    left: 60px;
    top: 100px;
    background: linear-gradient(160deg, var(--aqua) 0%, var(--aqua-deep) 100%);
  }
  .card--back {
    left: 580px;
    top: 480px;
    background: linear-gradient(135deg, var(--white) 0%, var(--paper) 55%, var(--paper-shade) 100%);
  }
  .brand {
    position: absolute;
    left: 50%;
    transform: translateX(-50%);
    display: flex;
    align-items: center;
    gap: 14px;
    white-space: nowrap;
  }
  .brand__dot {
    width: 54px;
    height: 54px;
    border-radius: 50%;
    flex: none;
  }
  .brand__name {
    font-size: 19px;
    font-weight: 700;
    letter-spacing: 0.3px;
  }
  .card--front .brand { top: 110px; }
  .card--front .brand__dot { background: var(--white); }
  .card--front .brand__name { color: var(--white); }
  .slogan {
    position: absolute;
    left: 0;
    right: 0;
    top: 196px;
    text-align: center;
    font-size: 17px;
    font-weight: 600;
    color: var(--ink);
  }
  .card--back .brand { top: 70px; }
  .card--back .brand__dot { background: var(--aqua); }
  .card--back .brand__name { color: var(--ink); }
  .contact {
    position: absolute;
    left: 90px;
    top: 150px;
    color: var(--aqua);
  }
  .contact__name {
    font-size: 32px;
    font-weight: 400;
    line-height: 1.1;
  }
  .contact__line {
    display: flex;
    align-items: baseline;
    gap: 8px;
    margin-top: 4px;
  }
  .contact__icon { width: 16px; height: 26px; align-self: center; }
  .contact__phone {
    font-size: 32px;
    font-weight: 400;
    letter-spacing: 0.5px;
  }
  .contact__note {
    font-size: 15px;
    color: var(--ink);
    margin-left: 4px;
  }
</style>
</head>
<body>
  <main class="canvas">
    <section class="card card--front">
      <div class="brand">
        <span class="brand__dot"></span>
        <span class="brand__name">Vantor Roving Car Wash and Detail Services</span>
      </div>
      <p class="slogan">I come to you, and wash your car wherever you are</p>
    </section>

    <section class="card card--back">
      <div class="brand">
        <span class="brand__dot"></span>
        <span class="brand__name">Vantor Roving Car Wash and Detail Services</span>
      </div>
      <div class="contact">
        <p class="contact__name">Oswin</p>
        <div class="contact__line">
          <svg class="contact__icon" viewBox="0 0 16 26" aria-hidden="true">
            <rect x="1.5" y="1.5" width="13" height="23" rx="2.5" fill="none" stroke="#5ccbdc" stroke-width="2"/>
            <line x1="6" y1="21" x2="10" y2="21" stroke="#5ccbdc" stroke-width="2" stroke-linecap="round"/>
          </svg>
          <span class="contact__phone">0471208356</span>
          <span class="contact__note">for an obligation free quote</span>
        </div>
      </div>
    </section>
  </main>
</body>
</html>
```